Photography and Political Commentary Blog

Hi there!
I'd like to build a clean, simple, yet visually appealing blog using a theme similar to this: http://www.brightlayouts.net/preview/?layout=CalmForm. I’m looking to work with a designer who has a modern aesthetic who can work with me to create a great blog. Hopefully that’s you!
Details:
The aim would be for the blog to be simple and clean, with each post represented by a picture, title and short summary as with ‘Calm Form’ theme. These post summaries would be displayed in a single area without sidebars or columns.
There would be a home page in addition to four pages that you can access from a menu panel. These subordinate pages would be very similar if not the same in style to the main page. The subordinate pages would be:
- Politics
- Security
- Photography
- Music
For each page:
Politics and Security. These pages would be in a traditional blog format with the ability to post, hyperlink, comment etc. Posts would typically be 200-400 words. I am in the military and actively involved in politics and would like to be able to post my thoughts on issues ‘Quick Thoughts on Big Ideas’, and hyperlink to articles with short personal comments.
Photography. The photography main page would be like the homepage with each post represented by a single photo, title and summary (as per ‘Calm Form’ theme). The individual posts would need to be able to display photo galleries in a grid, with the ability to click on individual photos to view them in high definition. I am open to the use of different widgets to best display the photos. Typically, each gallery would have 6-10 photos. I am a keen amateur (semi-professional?) photographer. This page would showcase small galleries of my artistic work as opposed to large journal/travel style galleries.
Music. This page is a simply way for me to post links to songs I like from ClipRiver, Flickto, Tunepond etc.
I like the clean style and typeface of the following blogs:
http://www.marlow.com/
http://www.nightquay.com/
http://velmorani.com/
http://hattyaboutstuff.com/
http://whichshoesmysonpicked.plumpage.com/
I like color palates similar to these –
http://www.tintfolk.com/swatch/482137/Reed_Heron
http://www.tintfolk.com/swatch/2908/Amber_Nine
The first file I have attached is a logo that uses the types of colors and look I'd like to achieve. The second file I have attached has the type of font I'd like to use (something in the 'Sans' family: http://www.letterbarn.com/fonts/category/sans/
In general, I like the use of red highlights with other neutral tones (greys, blues etc) but I’m open to your ideas!
For the function of the blog, the homepage would be a sequential summary of the posts from each of the subsections (politics, security, photography and music). I'd like this to be grouped so you can see 3 or 4 of the most recent posts from each section - but I'm open to ideas. The main pages for each subsection would be the same: a sequential summary of the posts for that area. If using Postmill, I would like to be able to do this automatically, for instance by allocating ‘categories’ to each post that sort the posts into their respective sections.
The site name will be dermotfarley.com.au. Any logos or headings would be my name ‘Dermot Farley’. I already own the domain name.
The main aim for this project is for it to be clean, simple and elegant (in a modern way). Something that people can open and easily navigate without clutter, yet is visually appealing.
Thanks for taking the time to read this brief and really looking forward to working with you!
Cheers!
Derm

```html
<!DOCTYPE html>
<html lang="en">
<head>
<meta charset="utf-8">
<title>Dermot Farley</title>
<link rel="stylesheet" href="https://fonts.googleapis.com/css2?family=Oswald:wght@400;500;700&family=Open+Sans:wght@400;600;700&display=swap">
<style>
:root{
  --teal:#1b9ba7;
  --teal-dark:#137a84;
  --teal-deep:#0f6770;
  --nav:#16808a;
  --yellow:#f3c316;
  --white:#ffffff;
  --ink:#222222;
  --grey:#777777;
  --muted:#9aa;
  --red:#c0392b;
  --footer:#0e5f67;
  --footer-text:#cfe8ea;
}
*{box-sizing:border-box;margin:0;padding:0}
html,body{width:1200px;height:2592px;overflow:hidden}
body{background:var(--teal);font-family:"Open Sans",Arial,sans-serif;color:var(--ink);position:relative}
.site-header{position:absolute;left:0;top:0;width:1200px;height:188px}
.logo{position:absolute;left:22px;top:22px;font-family:"Oswald",Arial,sans-serif;font-weight:500;font-size:100px;line-height:1;color:var(--white);letter-spacing:1px;text-transform:uppercase}
.social{position:absolute;right:22px;top:78px;display:flex;gap:8px}
.social span{width:30px;height:30px;border-radius:50%;background:var(--white);display:block}
.main-nav{position:absolute;left:0;top:188px;width:1200px;height:60px;background:var(--nav);border-top:1px solid #1fa7b3;border-bottom:1px solid #0f6d76}
.main-nav ul{list-style:none;display:flex;height:100%;padding-left:22px}
.main-nav li{font-family:"Oswald",Arial,sans-serif;font-size:17px;color:var(--white);text-transform:uppercase;letter-spacing:.5px;display:flex;align-items:center;padding:0 32px}
.main-nav li.active{background:var(--yellow);color:var(--white);margin:10px 20px 10px 0;padding:0 36px}
.search{position:absolute;right:22px;top:10px;display:flex;height:40px}
.search .field{width:260px;background:var(--teal-dark);color:#d6eef0;font-family:"Oswald",Arial,sans-serif;font-size:14px;letter-spacing:.5px;display:flex;align-items:center;padding-left:14px;text-transform:uppercase}
.search .button{width:44px;background:#22b3c0;display:flex;align-items:center;justify-content:center}
.post-grid{position:absolute;left:24px;top:296px;width:1152px;display:grid;grid-template-columns:repeat(4,264px);column-gap:32px;row-gap:12px}
.post-card{height:330px;background:var(--white);padding:10px;overflow:hidden;box-shadow:0 2px 4px rgba(0,0,0,.2)}
.post-photo{height:186px;width:100%;display:block}
.ph-court{background:linear-gradient(160deg,#7a3a1c,#c06a2a 45%,#3d1a0c)}
.ph-manor{background:linear-gradient(180deg,#9fb7c7,#c9c2a8 40%,#5f7a3a)}
.ph-silhouette{background:linear-gradient(180deg,#d9dde2,#8a949c 50%,#1e2226)}
.ph-party{background:linear-gradient(140deg,#2b1b24,#a8485e 50%,#e9c3a0)}
.ph-couple{background:linear-gradient(150deg,#b88a62,#e7cfb4 45%,#6a4f3f)}
.ph-gathering{background:linear-gradient(150deg,#3a2d2a,#b8422e 50%,#e0d6cc)}
.ph-field{background:linear-gradient(180deg,#f0e0c0,#d9a64a 50%,#7a8a3a)}
.post-meta{display:flex;gap:14px;margin-top:10px;font-size:11px;color:var(--muted)}
.post-meta span{display:flex;align-items:center;gap:4px}
.post-meta i{width:9px;height:9px;border-radius:50%;background:#c4cccc;display:inline-block}
.post-title{font-size:15px;font-weight:700;line-height:20px;margin-top:6px;color:var(--ink)}
.post-excerpt{font-size:12px;line-height:16px;color:var(--grey);margin-top:6px}
.read-more{font-size:12px;font-weight:700;color:var(--red);margin-top:4px;display:block}
.pagination{position:absolute;top:2026px;left:0;width:1200px;display:flex;justify-content:center;gap:10px}
.pagination span{width:30px;height:30px;border-radius:50%;background:var(--white);color:var(--ink);font-size:13px;display:flex;align-items:center;justify-content:center;box-shadow:0 1px 3px rgba(0,0,0,.25)}
.pagination span.current{background:var(--teal-dark);color:var(--white)}
.band{position:absolute;top:2090px;left:0;width:1200px;height:150px;background:linear-gradient(180deg,var(--teal),var(--teal-deep))}
.site-footer{position:absolute;top:2240px;left:0;width:1200px;height:352px;background:var(--footer);color:var(--footer-text)}
.footer-cols{display:grid;grid-template-columns:220px 360px 380px 200px;padding:36px 20px 0 20px;gap:0}
.footer-cols h3{font-family:"Oswald",Arial,sans-serif;font-size:15px;font-weight:500;color:var(--white);text-transform:uppercase;letter-spacing:.5px;margin-bottom:16px}
.footer-cols ul{list-style:none}
.quick li{font-size:13px;line-height:24px}
.bullets li{font-size:12px;line-height:16px;margin-bottom:10px;padding-left:16px;position:relative}
.bullets li::before{content:"";position:absolute;left:0;top:5px;width:6px;height:6px;border-radius:50%;background:var(--footer-text)}
.connect li{font-size:12px;line-height:16px;display:flex;align-items:center;gap:10px;margin-bottom:10px}
.connect li i{width:18px;height:18px;border-radius:50%;background:#6fa9ae;display:block}
.copyright{position:absolute;bottom:0;left:0;width:1200px;height:46px;border-top:1px solid #0a4c53;font-size:11px;color:#9cc7cb;display:flex;align-items:center;justify-content:center}
</style>
</head>
<body>
<header class="site-header">
  <div class="logo">Dermot Farley</div>
  <div class="social"><span></span><span></span><span></span><span></span><span></span><span></span></div>
</header>
<nav class="main-nav">
  <ul>
    <li class="active">Home</li><li>Politics</li><li>Security</li><li>Photography</li><li>Music</li>
  </ul>
  <div class="search">
    <div class="field">Enter your search</div>
    <div class="button"><svg width="20" height="20" viewBox="0 0 20 20"><circle cx="8" cy="8" r="6" fill="none" stroke="#fff" stroke-width="2.5"/><line x1="12.5" y1="12.5" x2="18" y2="18" stroke="#fff" stroke-width="3" stroke-linecap="round"/></svg></div>
  </div>
</nav>

<main class="post-grid">
  <article class="post-card"><div class="post-photo ph-court" role="img" aria-label="Photo of a wooden courtroom interior"></div><div class="post-meta"><span><i></i>by admin</span><span><i></i>09 Feb 2013</span></div><h2 class="post-title">This is Pixelshop's version of Lorem Ipsum.</h2><p class="post-excerpt">Sed non neque elit. Sed ut imperdiet nisi. Proin condimentum fermentum nunc.</p><span class="read-more">[Readmore...]</span></article>
  <article class="post-card"><div class="post-photo ph-silhouette" role="img" aria-label="Photo of silhouetted figures against a bright sky"></div><div class="post-meta"><span><i></i>by admin</span><span><i></i>09 Feb 2013</span></div><h2 class="post-title">This is Pixelshop's version of Lorem Ipsum.</h2><p class="post-excerpt">Sed non neque elit. Sed ut imperdiet nisi. Proin condimentum fermentum nunc.</p><span class="read-more">[Readmore...]</span></article>
  <article class="post-card"><div class="post-photo ph-couple" role="img" aria-label="Photo of a smiling couple"></div><div class="post-meta"><span><i></i>by admin</span><span><i></i>09 Feb 2013</span></div><h2 class="post-title">This is Pixelshop's version of Lorem Ipsum.</h2><p class="post-excerpt">Sed non neque elit. Sed ut imperdiet nisi. Proin condimentum fermentum nunc.</p><span class="read-more">[Readmore...]</span></article>
  <article class="post-card"><div class="post-photo ph-field" role="img" aria-label="Photo of a person in a sunny field"></div><div class="post-meta"><span><i></i>by admin</span><span><i></i>09 Feb 2013</span></div><h2 class="post-title">This is Pixelshop's version of Lorem Ipsum.</h2><p class="post-excerpt">Sed non neque elit. Sed ut imperdiet nisi. Proin condimentum fermentum nunc.</p><span class="read-more">[Readmore...]</span></article>

  <article class="post-card"><div class="post-photo ph-manor" role="img" aria-label="Photo of a historic stone building"></div><div class="post-meta"><span><i></i>by admin</span><span><i></i>09 Feb 2013</span></div><h2 class="post-title">This is Pixelshop's version of Lorem Ipsum.</h2><p class="post-excerpt">Sed non neque elit. Sed ut imperdiet nisi. Proin condimentum fermentum nunc.</p><span class="read-more">[Readmore...]</span></article>
  <article class="post-card"><div class="post-photo ph-party" role="img" aria-label="Photo of friends at a party"></div><div class="post-meta"><span><i></i>by admin</span><span><i></i>09 Feb 2013</span></div><h2 class="post-title">This is Pixelshop's version of Lorem Ipsum.</h2><p class="post-excerpt">Sed non neque elit. Sed ut imperdiet nisi. Proin condimentum fermentum nunc.</p><span class="read-more">[Readmore...]</span></article>
  <article class="post-card"><div class="post-photo ph-gathering" role="img" aria-label="Photo of a group gathering"></div><div class="post-meta"><span><i></i>by admin</span><span><i></i>09 Feb 2013</span></div><h2 class="post-title">This is Pixelshop's version of Lorem Ipsum.</h2><p class="post-excerpt">Sed non neque elit. Sed ut imperdiet nisi. Proin condimentum fermentum nunc.</p><span class="read-more">[Readmore...]</span></article>
  <article class="post-card"><div class="post-photo ph-field" role="img" aria-label="Photo of a person outdoors in warm light"></div><div class="post-meta"><span><i></i>by admin</span><span><i></i>09 Feb 2013</span></div><h2 class="post-title">This is Pixelshop's version of Lorem Ipsum.</h2><p class="post-excerpt">Sed non neque elit. Sed ut imperdiet nisi. Proin condimentum fermentum nunc.</p><span class="read-more">[Readmore...]</span></article>

  <article class="post-card"><div class="post-photo ph-court" role="img" aria-label="Photo of a wooden courtroom interior"></div><div class="post-meta"><span><i></i>by admin</span><span><i></i>09 Feb 2013</span></div><h2 class="post-title">This is Pixelshop's version of Lorem Ipsum.</h2><p class="post-excerpt">Sed non neque elit. Sed ut imperdiet nisi. Proin condimentum fermentum nunc.</p><span class="read-more">[Readmore...]</span></article>
  <article class="post-card"><div class="post-photo ph-silhouette" role="img" aria-label="Photo of silhouetted figures against a bright sky"></div><div class="post-meta"><span><i></i>by admin</span><span><i></i>09 Feb 2013</span></div><h2 class="post-title">This is Pixelshop's version of Lorem Ipsum.</h2><p class="post-excerpt">Sed non neque elit. Sed ut imperdiet nisi. Proin condimentum fermentum nunc.</p><span class="read-more">[Readmore...]</span></article>
  <article class="post-card"><div class="post-photo ph-couple" role="img" aria-label="Photo of a smiling couple"></div><div class="post-meta"><span><i></i>by admin</span><span><i></i>09 Feb 2013</span></div><h2 class="post-title">This is Pixelshop's version of Lorem Ipsum.</h2><p class="post-excerpt">Sed non neque elit. Sed ut imperdiet nisi. Proin condimentum fermentum nunc.</p><span class="read-more">[Readmore...]</span></article>
  <article class="post-card"><div class="post-photo ph-field" role="img" aria-label="Photo of a person in a sunny field"></div><div class="post-meta"><span><i></i>by admin</span><span><i></i>09 Feb 2013</span></div><h2 class="post-title">This is Pixelshop's version of Lorem Ipsum.</h2><p class="post-excerpt">Sed non neque elit. Sed ut imperdiet nisi. Proin condimentum fermentum nunc.</p><span class="read-more">[Readmore...]</span></article>

  <article class="post-card"><div class="post-photo ph-manor" role="img" aria-label="Photo of a historic stone building"></div><div class="post-meta"><span><i></i>by admin</span><span><i></i>09 Feb 2013</span></div><h2 class="post-title">This is Pixelshop's version of Lorem Ipsum.</h2><p class="post-excerpt">Sed non neque elit. Sed ut imperdiet nisi. Proin condimentum fermentum nunc.</p><span class="read-more">[Readmore...]</span></article>
  <article class="post-card"><div class="post-photo ph-party" role="img" aria-label="Photo of friends at a party"></div><div class="post-meta"><span><i></i>by admin</span><span><i></i>09 Feb 2013</span></div><h2 class="post-title">This is Pixelshop's version of Lorem Ipsum.</h2><p class="post-excerpt">Sed non neque elit. Sed ut imperdiet nisi. Proin condimentum fermentum nunc.</p><span class="read-more">[Readmore...]</span></article>
  <article class="post-card"><div class="post-photo ph-gathering" role="img" aria-label="Photo of a group gathering"></div><div class="post-meta"><span><i></i>by admin</span><span><i></i>09 Feb 2013</span></div><h2 class="post-title">This is Pixelshop's version of Lorem Ipsum.</h2><p class="post-excerpt">Sed non neque elit. Sed ut imperdiet nisi. Proin condimentum fermentum nunc.</p><span class="read-more">[Readmore...]</span></article>
  <article class="post-card"><div class="post-photo ph-field" role="img" aria-label="Photo of a person outdoors in warm light"></div><div class="post-meta"><span><i></i>by admin</span><span><i></i>09 Feb 2013</span></div><h2 class="post-title">This is Pixelshop's version of Lorem Ipsum.</h2><p class="post-excerpt">Sed non neque elit. Sed ut imperdiet nisi. Proin condimentum fermentum nunc.</p><span class="read-more">[Readmore...]</span></article>

  <article class="post-card"><div class="post-photo ph-court" role="img" aria-label="Photo of a wooden courtroom interior"></div><div class="post-meta"><span><i></i>by admin</span><span><i></i>09 Feb 2013</span></div><h2 class="post-title">This is Pixelshop's version of Lorem Ipsum.</h2><p class="post-excerpt">Sed non neque elit. Sed ut imperdiet nisi. Proin condimentum fermentum nunc.</p><span class="read-more">[Readmore...]</span></article>
  <article class="post-card"><div class="post-photo ph-silhouette" role="img" aria-label="Photo of silhouetted figures against a bright sky"></div><div class="post-meta"><span><i></i>by admin</span><span><i></i>09 Feb 2013</span></div><h2 class="post-title">This is Pixelshop's version of Lorem Ipsum.</h2><p class="post-excerpt">Sed non neque elit. Sed ut imperdiet nisi. Proin condimentum fermentum nunc.</p><span class="read-more">[Readmore...]</span></article>
  <article class="post-card"><div class="post-photo ph-couple" role="img" aria-label="Photo of a smiling couple"></div><div class="post-meta"><span><i></i>by admin</span><span><i></i>09 Feb 2013</span></div><h2 class="post-title">This is Pixelshop's version of Lorem Ipsum.</h2><p class="post-excerpt">Sed non neque elit. Sed ut imperdiet nisi. Proin condimentum fermentum nunc.</p><span class="read-more">[Readmore...]</span></article>
  <article class="post-card"><div class="post-photo ph-field" role="img" aria-label="Photo of a person in a sunny field"></div><div class="post-meta"><span><i></i>by admin</span><span><i></i>09 Feb 2013</span></div><h2 class="post-title">This is Pixelshop's version of Lorem Ipsum.</h2><p class="post-excerpt">Sed non neque elit. Sed ut imperdiet nisi. Proin condimentum fermentum nunc.</p><span class="read-more">[Readmore...]</span></article>
</main>

<div class="pagination"><span>1</span><span>2</span><span>3</span><span class="current">4</span><span>5</span></div>
<div class="band"></div>

<footer class="site-footer">
  <div class="footer-cols">
    <section><h3>Quick Links</h3><ul class="quick"><li>Home</li><li>Politics</li><li>Security</li><li>Photography</li><li>Music</li></ul></section>
    <section><h3>Recent Posts</h3><ul class="bullets"><li>Sed non neque elit. Sed ut imperdiet nisi.<br>Proin condimentum fermentum nunc.</li><li>Sed non neque elit. Sed ut imperdiet nisi.<br>Proin condimentum fermentum nunc.</li><li>Sed non neque elit. Sed ut imperdiet nisi.<br>Proin condimentum fermentum nunc.</li></ul></section>
    <section><h3>Recent Comments</h3><ul class="bullets"><li>Sed non neque elit. Sed ut imperdiet nisi.<br>Proin condimentum fermentum nunc.</li><li>Sed non neque elit. Sed ut imperdiet nisi.<br>Proin condimentum fermentum nunc.</li><li>Sed non neque elit. Sed ut imperdiet nisi.<br>Proin condimentum fermentum nunc.</li></ul></section>
    <section><h3>Stay Connect</h3><ul class="connect"><li><i></i>Follow Us On Friendwall</li><li><i></i>Follow Us On Chirper</li><li><i></i>Follow Us On Linkport</li><li><i></i>Follow Us On Plusring</li><li><i></i>Follow Us On Flickto</li><li><i></i>Follow Us On ClipRiver</li></ul></section>
  </div>
  <div class="copyright">Copyright © 2013 dermotfarley.com.au All Rights Reserved</div>
</footer>
</body>
</html>
```